Apartments rental business needs a web for direct reservations.

I need a website that allows my clients to check the property (pictures, a brief description etc) and lets them make reservations. They will be providing the required information such as name, last name, email address and credit card details. Also a calendar where I can update the availability (dates and prices) of the property upon new reservations is a must. I already have a logo that should also be a good starting point for colors, style an inspiration.

Need extra days to review

```html
<!DOCTYPE html>
<html lang="en">
<head>
<meta charset="utf-8">
<title>Larkspur Bungalows – Reservations</title>
<link href="https://fonts.googleapis.com/css2?family=Montserrat:wght@400;500;600;700&family=Open+Sans:wght@400;600&display=swap" rel="stylesheet">
<style>
:root{
  --peach:#f2703c;
  --teal:#2aa79b;
  --ink:#3b3b3b;
  --muted:#8a8a8a;
  --line:#e3e3e3;
  --soft:#f6f6f6;
  --footer:#323234;
  --field:#4a4a4c;
}
*{box-sizing:border-box;margin:0;padding:0}
html,body{width:1200px;height:3508px;overflow:hidden}
body{position:relative;background:#fff;font-family:"Open Sans",Arial,sans-serif;color:var(--ink);font-size:14px}
.abs{position:absolute}
h2.section-title{font-family:"Montserrat",sans-serif;font-weight:600;font-size:26px;letter-spacing:1px;text-transform:uppercase;color:var(--teal);white-space:nowrap}
h2.section-title span{color:var(--peach)}

/* header */
.site-header{left:0;top:0;width:1200px;height:100px;display:flex;align-items:center;padding:0 60px;background:#fff}
.brand{display:flex;align-items:center;gap:10px;font-family:"Montserrat",sans-serif;font-weight:700;font-size:24px;color:var(--peach);letter-spacing:1px}
.brand i{width:26px;height:26px;border-radius:50%;background:var(--teal);display:block}
.header-right{margin-left:auto;display:flex;flex-direction:column;align-items:flex-end;gap:12px}
.header-top{display:flex;align-items:center;gap:12px;font-size:13px;font-family:"Montserrat",sans-serif;white-space:nowrap}
.social{width:26px;height:26px;border-radius:50%;background:var(--peach);display:inline-block}
.social.alt{background:var(--teal)}
.btn{display:inline-block;background:var(--peach);color:#fff;font-family:"Montserrat",sans-serif;font-weight:600;font-size:12px;text-transform:uppercase;letter-spacing:.5px;padding:9px 18px;border-radius:20px;white-space:nowrap}
.btn.teal{background:var(--teal)}
.main-nav{display:flex;gap:44px;font-family:"Montserrat",sans-serif;font-size:12px;text-transform:uppercase;color:var(--ink)}
.main-nav a{color:inherit;text-decoration:none}
.main-nav a.active{color:var(--peach)}

/* hero */
.hero{left:0;top:100px;width:1200px;height:510px;background:linear-gradient(180deg,#6f7e5a 0%,#8f9a7a 35%,#c9ccc6 58%,#5fa6c4 75%,#7a6652 100%)}
.gallery{left:0;top:620px;width:1200px;height:180px}
.thumb{position:absolute;top:20px;width:160px;height:150px}
.arrow{position:absolute;top:84px;width:24px;height:24px;border-radius:50%;background:#d6d6d6}

/* intro */
.intro{left:0;top:840px;width:1200px;text-align:center}
.intro p{width:1000px;margin:22px auto 24px;font-size:14px;line-height:24px;color:var(--muted)}
.features{left:100px;top:1120px;width:1000px;display:flex;justify-content:space-around;padding:30px 0;border-top:1px solid var(--line);border-bottom:1px solid var(--line)}
.feature{text-align:center;font-size:13px;color:var(--ink)}
.feature svg{display:block;margin:0 auto 10px}

/* facilities and calendar */
.facilities{left:90px;top:1290px;width:500px}
.facility-list{margin-top:30px;list-style:none}
.facility-list li{display:flex;align-items:center;gap:14px;height:40px;border-bottom:1px solid var(--line);font-size:13px}
.facility-list li::before{content:"";width:20px;height:16px;border:2px solid var(--ink);border-radius:3px}
.availability{left:615px;top:1290px;width:500px}
.calendar{margin-top:30px;border:1px solid var(--line);padding:20px}
.cal-grid{display:grid;grid-template-columns:repeat(7,1fr);row-gap:26px;text-align:center;font-size:13px;margin-top:20px}
.cal-grid .on{background:var(--ink);color:#fff;border-radius:50%;width:26px;height:26px;line-height:26px;margin:auto}

/* testimonials */
.testimonials{left:90px;top:2170px;width:1020px;text-align:center}
.reviews{display:flex;gap:30px;margin-top:40px;text-align:left}
.review{flex:1;height:230px;background:#fff;box-shadow:0 2px 10px rgba(0,0,0,.12);padding:30px;display:flex;gap:20px}
.avatar{width:72px;height:72px;border-radius:50%;background:var(--teal);flex:none}
.review h4{font-family:"Montserrat",sans-serif;font-size:16px}
.review small{color:var(--muted);font-size:12px}
.review p{margin-top:20px;font-size:13px;line-height:21px;color:var(--muted)}
.stars{color:var(--peach);margin-top:12px;letter-spacing:3px}
.dots{display:flex;justify-content:center;gap:10px;margin-top:40px}
.dots i{width:22px;height:22px;border-radius:50%;background:#d6d6d6;display:block}
.dots i.on{background:var(--peach)}

.map{left:0;top:2600px;width:1200px;height:290px;background:linear-gradient(135deg,#eeece6,#e2e0d8 50%,#ece9e2)}

/* footer */
.site-footer{left:0;top:2890px;width:1200px;height:618px;background:var(--footer);color:#cfcfcf}
.footer-col{position:absolute;top:60px}
.footer-col h3{font-family:"Montserrat",sans-serif;font-size:18px;color:#fff;font-weight:600;margin-bottom:24px}
.footer-col p,.footer-col li{font-size:13px;line-height:26px;list-style:none}
.footer-phone{font-family:"Montserrat",sans-serif;font-size:22px;color:#fff;margin-bottom:14px;white-space:nowrap}
.ffield{height:40px;background:var(--field);border-radius:3px;margin-bottom:14px}
.copyright{position:absolute;left:90px;top:470px;font-size:12px;color:#9a9a9a}
.to-top{position:absolute;right:90px;top:466px;width:20px;height:20px}

/* dim layer */
.dim{left:0;top:0;width:1200px;height:3508px;background:rgba(70,70,70,.45)}

/* reservation modal */
.modal{left:205px;top:1395px;width:790px;height:655px;background:#fff;box-shadow:0 10px 40px rgba(0,0,0,.35)}
.modal-title{height:70px;display:flex;align-items:center;justify-content:center;border-bottom:1px solid var(--line)}
.close{position:absolute;right:-14px;top:-14px;width:32px;height:32px;border-radius:50%;background:var(--peach);color:#fff;text-align:center;line-height:30px;font-size:18px;font-family:"Montserrat",sans-serif}
.modal-body{padding:20px 30px}
.modal h3{font-family:"Montserrat",sans-serif;font-size:15px;font-weight:600;margin-bottom:18px}
.row{display:flex;gap:16px;margin-bottom:12px}
.input{flex:1;height:36px;border:1px solid var(--line);border-radius:3px;font-size:12px;color:#aaa;padding:9px 12px;white-space:nowrap;overflow:hidden}
.textarea{height:64px}
.pay-head{display:flex;justify-content:space-between;align-items:center;margin-top:24px;padding-top:20px;border-top:1px solid var(--line)}
.cards{display:flex;gap:6px}
.cards i{width:34px;height:20px;border-radius:3px;background:#c7c7c7;display:block}
.cards i:nth-child(2n){background:#9aa9b8}
.label{font-size:12px;margin-bottom:6px;white-space:nowrap}
.pay-row{display:flex;gap:16px}
.pay-row>div{display:flex;flex-direction:column}
.submit{display:block;width:190px;margin:30px auto 0;text-align:center}
</style>
</head>
<body>

<header class="site-header abs">
  <div class="brand"><i></i>LARKSPUR</div>
  <div class="header-right">
    <div class="header-top">
      <span>Call Us: 555 0142 386</span>
      <span class="social"></span><span class="social alt"></span><span class="social"></span>
      <span class="btn teal">Make a Reservation</span>
    </div>
    <nav class="main-nav">
      <a class="active" href="#">Home</a><a href="#">Accommodation</a><a href="#">Facilities</a><a href="#">Location</a><a href="#">Contact Us</a>
    </nav>
  </div>
</header>

<div class="hero abs" role="img" aria-label="Photo of the outdoor swimming pool with loungers and palm trees"></div>

<section class="gallery abs">
  <span class="arrow" style="left:30px"></span>
  <div class="thumb" role="img" aria-label="Bungalow exterior" style="left:85px;background:#8c9a78"></div>
  <div class="thumb" role="img" aria-label="Pool view" style="left:260px;background:#6e9fb6"></div>
  <div class="thumb" role="img" aria-label="Garden path" style="left:435px;background:#a3a894"></div>
  <div class="thumb" role="img" aria-label="Red brick bungalow" style="left:610px;background:#a8563a"></div>
  <div class="thumb" role="img" aria-label="Patio seating" style="left:785px;background:#8a7765"></div>
  <div class="thumb" role="img" aria-label="Bedroom interior" style="left:960px;background:#c9c6c0"></div>
  <span class="arrow" style="right:30px"></span>
</section>

<section class="intro abs">
  <h2 class="section-title"><span>The Larkspur</span> Bungalows</h2>
  <p>Our bungalows sit in a quiet garden setting just a short walk from the beach, shops and cafes. Each unit offers a private patio, a fully equipped kitchen and comfortable bedding. Guests can relax by the outdoor pool, enjoy free parking and fast wifi, and explore the nearby walking trails. Friendly staff are on hand to help you plan your stay, and direct bookings always receive our best available rates for every season.</p>
  <span class="btn">Book a Reservation</span>
</section>

<div class="features abs">
  <div class="feature"><svg width="40" height="32" viewBox="0 0 40 32" fill="none" stroke="#2aa79b" stroke-width="2"><path d="M4 22c4-3 8 3 12 0s8 3 12 0 8 3 8 0M4 28c4-3 8 3 12 0s8 3 12 0 8 3 8 0M12 18V4h8M24 18V4"/></svg>Swimming Pool</div>
  <div class="feature"><svg width="40" height="32" viewBox="0 0 40 32" fill="none" stroke="#2aa79b" stroke-width="2"><path d="M4 12a22 22 0 0 1 32 0M9 17a15 15 0 0 1 22 0M14 22a8 8 0 0 1 12 0"/><circle cx="20" cy="27" r="2" fill="#2aa79b"/></svg>Free WiFi</div>
  <div class="feature"><svg width="40" height="32" viewBox="0 0 40 32" fill="none" stroke="#2aa79b" stroke-width="2"><rect x="8" y="2" width="24" height="28" rx="4"/><path d="M16 24V8h6a5 5 0 0 1 0 10h-6"/></svg>Free Parking</div>
  <div class="feature"><svg width="40" height="32" viewBox="0 0 40 32" fill="none" stroke="#2aa79b" stroke-width="2"><circle cx="20" cy="16" r="13"/><path d="M11 7l18 18M10 16h16"/></svg>Non-Smoking Rooms</div>
</div>

<section class="facilities abs">
  <h2 class="section-title"><span>Most</span> Popular Facilities</h2>
  <ul class="facility-list">
    <li>Room Amenities</li><li>Activities</li><li>Wheelchair Access</li><li>Bedding</li><li>Restaurant</li><li>Living Area</li><li>Free Parking</li><li>Media &amp; Technology</li><li>Internet</li><li>General</li><li>Outdoors</li><li>Pool</li><li>Bathroom</li><li>Languages Spoken</li>
  </ul>
</section>

<section class="availability abs">
  <h2 class="section-title"><span>Check</span> Available Dates</h2>
  <div class="calendar">
    <div style="display:flex;justify-content:space-between;font-family:Montserrat,sans-serif;font-weight:600"><span>‹</span><span>June 2024</span><span>›</span></div>
    <div class="cal-grid">
      <b>Mon</b><b>Tue</b><b>Wed</b><b>Thu</b><b>Fri</b><b>Sat</b><b>Sun</b>
      <span></span><span></span><span></span><span></span><span></span><span>1</span><span>2</span>
      <span>3</span><span>4</span><span>5</span><span>6</span><span>7</span><span>8</span><span>9</span>
      <span>10</span><span>11</span><span>12</span><span>13</span><span>14</span><span>15</span><span class="on">16</span>
      <span>17</span><span>18</span><span>19</span><span>20</span><span>21</span><span>22</span><span>23</span>
      <span>24</span><span>25</span><span>26</span><span>27</span><span>28</span><span>29</span><span>30</span>
    </div>
  </div>
</section>

<section class="testimonials abs">
  <h2 class="section-title"><span>What</span> Customers Are Saying</h2>
  <div class="reviews">
    <div class="review"><div class="avatar" role="img" aria-label="Guest portrait"></div><div><h4>Harriet</h4><small>Guest</small><p>A lovely quiet stay with a spotless bungalow and a great pool. Staff were warm and helpful throughout.</p><div class="stars">★★★★★</div></div></div>
    <div class="review"><div class="avatar" role="img" aria-label="Guest portrait"></div><div><h4>Jonah</h4><small>Guest</small><p>Perfect location close to the beach. Booking online was quick and simple, we will return next year.</p><div class="stars">★★★★★</div></div></div>
    <div class="review"><div class="avatar" role="img" aria-label="Guest portrait"></div><div><h4>Priya</h4><small>Guest</small><p>Comfortable beds, a well stocked kitchen and a relaxing garden. Great value for a family holiday.</p><div class="stars">★★★★★</div></div></div>
  </div>
  <div class="dots"><i></i><i class="on"></i><i></i></div>
</section>

<div class="map abs" role="img" aria-label="Street map showing the bungalows location"></div>

<footer class="site-footer abs">
  <div class="footer-col" style="left:90px;width:280px">
    <h3>Contact Us</h3>
    <div class="footer-phone">Call: 555 - 0142 - 386</div>
    <p>14 Garden Lane, Seaview<br>Coastal Bay 4020</p>
    <p style="color:var(--peach)">hello@larkspur.example</p>
    <div style="display:flex;gap:10px;margin-top:20px"><span class="social"></span><span class="social"></span><span class="social"></span></div>
  </div>
  <div class="footer-col" style="left:400px">
    <h3>Quick Links</h3>
    <ul><li>Home</li><li>Accommodation</li><li>Facilities</li><li>Location</li><li>Contact Us</li><li>Terms &amp; Conditions</li><li>Privacy Policy</li></ul>
  </div>
  <div class="footer-col" style="left:615px;width:500px">
    <h3>How Can We Help?</h3>
    <div style="display:flex;gap:14px"><div class="ffield" style="flex:1"></div><div class="ffield" style="flex:1"></div></div>
    <div class="ffield"></div>
    <div class="ffield" style="height:70px"></div>
    <span class="btn teal">Submit</span>
  </div>
  <div class="copyright">© 2024 Larkspur Bungalows. All Rights Reserved.</div>
  <svg class="to-top" viewBox="0 0 20 20" fill="none" stroke="#9a9a9a" stroke-width="2"><path d="M10 17V3M4 9l6-6 6 6"/></svg>
</footer>

<div class="dim abs"></div>

<div class="modal abs" role="dialog" aria-label="Make a reservation">
  <span class="close">×</span>
  <div class="modal-title"><h2 class="section-title"><span>Make</span> a Reservations</h2></div>
  <div class="modal-body">
    <h3>Personal Details</h3>
    <div class="row"><div class="input">First name</div><div class="input">Last name</div></div>
    <div class="row"><div class="input">Email</div><div class="input">Phone</div></div>
    <div class="row"><div class="input">Address</div><div class="input">City</div></div>
    <div class="row"><div class="input">Zip/Post Code</div><div class="input">Country</div></div>
    <div class="row"><div class="input textarea">Type Your Message Here...</div></div>
    <div class="pay-head"><h3 style="margin:0">Payment Details</h3><div class="cards"><i></i><i></i><i></i><i></i><i></i><i></i></div></div>
    <div class="pay-row" style="margin-top:16px">
      <div style="width:150px"><span class="label">Card Type*</span><div class="input">Select</div></div>
      <div style="width:190px"><span class="label">Card Number*</span><div class="input">Card Number</div></div>
      <div style="width:200px"><span class="label">Expiry Date*</span><div style="display:flex;gap:8px"><div class="input">Month</div><div class="input">Year</div></div></div>
      <div style="width:120px"><span class="label">CVC Code*</span><div class="input">CVC</div></div>
    </div>
    <span class="btn submit">Complete Booking</span>
  </div>
</div>

</body>
</html>
```